Business card for a shipping supplies business

Needing a business card design. Please see the logo. The logo with the white font should be used if there is a dark background.

We are looking for the following info on the card. Please see the sample info. We will need the info to be changed with a few different employee names and info but all will use the same template.

Business Name: The Crate Heron
Employee Name : Derek Malloy
Position: Account Manager
Address: 4827 W. Ridge 918 S.
Fort Worth, TX 72348
email: Derek@thecrateheron.com
telephone: 866-417-2902 x 217
website: www.getcartonry.com

Target Market(s)

Businesses who ship products for online sales

Industry/Entity Type

Cardboard

Contact Information for Business Card

Name, title, address, website, logo, telephone number

Font styles to use
Sans Serif

Colors
EE7325
F08F49
F5BC92
FAE3D3
FDF4ED

Requirements
Must have
• Logo on back of card. Clean look, just logo, website address

```html
<!DOCTYPE html>
<html lang="en">
<head>
<meta charset="utf-8">
<title>The Crate Heron — Business Card</title>
<link rel="stylesheet" href="https://fonts.googleapis.com/css2?family=Jost:wght@400;500;600;700&display=swap">
<style>
  :root {
    --navy: #041821;
    --orange: #E2642A;
    --orange-light: #F08F49;
    --orange-pale: #F5BC92;
    --paper: #ffffff;
    --stage: #f4f4f4;
    --ink: #1c1c1c;
    --muted-teal: #9fb3bb;
  }
  * { margin: 0; padding: 0; box-sizing: border-box; }
  html, body { width: 1200px; height: 1200px; overflow: hidden; }
  body {
    background: var(--stage);
    font-family: "Jost", sans-serif;
    position: relative;
  }
  .card {
    position: absolute;
    top: 90px;
    width: 498px;
    height: 285px;
    overflow: hidden;
  }
  /* Back of card */
  .card-back { left: 81px; background: var(--navy); }
  .card-back .brand-mark {
    position: absolute; left: 219px; top: 62px;
    width: 60px; height: 60px; border-radius: 50%;
    background: var(--orange);
  }
  .card-back .brand-name {
    position: absolute; left: 0; right: 0; top: 144px;
    text-align: center; color: #fff;
    font-weight: 600; font-size: 34px; letter-spacing: 0.5px;
  }
  .card-back .website {
    position: absolute; left: 0; right: 0; top: 226px;
    text-align: center; color: var(--muted-teal);
    font-size: 26px; letter-spacing: 0.5px;
  }
  /* Front of card */
  .card-front { left: 636px; background: var(--paper); border: 1px solid #d8d8d8; }
  .card-front .contact {
    position: absolute; left: 46px; top: 34px; color: var(--ink);
  }
  .company {
    color: var(--orange); font-weight: 600; font-size: 23px;
    text-transform: uppercase; letter-spacing: 0.5px; line-height: 28px;
  }
  .person { margin-top: 10px; font-weight: 600; font-size: 17px; line-height: 22px; }
  .role { font-size: 17px; line-height: 22px; }
  .address { margin-top: 24px; font-size: 18px; line-height: 22px; }
  .channels { margin-top: 4px; list-style: none; }
  .channels li {
    display: flex; align-items: center; gap: 8px;
    font-size: 16.5px; line-height: 23.5px;
  }
  .channels svg { width: 16px; height: 16px; flex: none; }
  .brand-panel {
    position: absolute; left: 314px; top: 0; width: 184px; height: 285px;
    background: var(--navy);
  }
  .brand-panel .brand-mark {
    position: absolute; left: 68px; top: 44px;
    width: 48px; height: 48px; border-radius: 50%;
    background: var(--orange);
  }
  .brand-panel .brand-name {
    position: absolute; left: 0; right: 0; top: 112px;
    text-align: center; color: #fff;
    font-weight: 600; font-size: 18px;
  }
  .tail-art { position: absolute; left: 296px; top: 182px; width: 202px; height: 103px; }
</style>
</head>
<body>

  <section class="card card-back" aria-label="Business card back">
    <span class="brand-mark"></span>
    <p class="brand-name">The Crate Heron</p>
    <p class="website">www.getcartonry.com</p>
  </section>

  <section class="card card-front" aria-label="Business card front">
    <div class="contact">
      <p class="company">The Crate Heron</p>
      <p class="person">Derek Malloy</p>
      <p class="role">Account Manager</p>
      <p class="address">4827 W. Ridge 918 S.<br>Fort Worth, TX 72348</p>
      <ul class="channels">
        <li>
          <svg viewBox="0 0 16 16" aria-hidden="true"><rect x="1.5" y="3.5" width="13" height="9" fill="none" stroke="#E2642A" stroke-width="1.4"/><path d="M1.5 3.5 L8 9 L14.5 3.5" fill="none" stroke="#E2642A" stroke-width="1.4"/></svg>
          Derek@thecrateheron.com
        </li>
        <li>
          <svg viewBox="0 0 16 16" aria-hidden="true"><path d="M4 1.5 L6.5 4.5 L5 6.5 C6 9 7.5 10.5 9.5 11.5 L11.5 10 L14.5 12.5 L12.5 14.5 C7 14 2 9 1.5 3.5 Z" fill="#E2642A"/></svg>
          866-417-2902 x 217
        </li>
        <li>
          <svg viewBox="0 0 16 16" aria-hidden="true"><circle cx="8" cy="8" r="6.5" fill="none" stroke="#E2642A" stroke-width="1.4"/><ellipse cx="8" cy="8" rx="2.8" ry="6.5" fill="none" stroke="#E2642A" stroke-width="1.2"/><path d="M1.5 8 H14.5 M2.8 4.8 H13.2 M2.8 11.2 H13.2" stroke="#E2642A" stroke-width="1.1"/></svg>
          www.getcartonry.com
        </li>
      </ul>
    </div>

    <div class="brand-panel">
      <span class="brand-mark"></span>
      <p class="brand-name">The Crate Heron</p>
    </div>

    <svg class="tail-art" viewBox="0 0 202 103" role="img" aria-label="Sweeping orange tail illustration in the lower corner">
      <defs>
        <linearGradient id="tailTone" x1="0" y1="1" x2="1" y2="0">
          <stop offset="0" stop-color="#E2642A"/>
          <stop offset="1" stop-color="#F08F49"/>
        </linearGradient>
      </defs>
      <path d="M0 103 C10 60 40 35 90 32 C140 30 175 20 202 0 L202 103 Z" fill="url(#tailTone)"/>
    </svg>
  </section>

</body>
</html>
```